Custom Mexican Train Dominos Scorecard

My wife and I regularly play Mexican Train dominos with our friends and family and would like to create a series of custom scorecards specific to our various groups that we play with. The idea would be to have them printed on pads or in notebooks that over time will hold a record of all of our games. Searching around on the web, the only "off the shelf" that I see are pretty plain and boring (see attached). We would love something with a fun and playful mid-century graphic feel to it. Can be a single color or more than one. We want to have the player names incorporated into the design, so for the first one the names would be Tessa, Harold, Ruth & Colin. We will want a place to date each card and of course boxes to fill out the score. I have included a few examples of how the scorecard is basically laid out. Can be any size and can be done in landscape or portrait. I think I would just like the title to say "Domino Night" or potentially no title at all with just a fun domino graphic. Thank you!

Requirements
Must have
• Basic score layout
Nice to have
• nothing in particular
Should not have
• nothing in particular

```html
<!DOCTYPE html>
<html lang="en">
<head>
<meta charset="utf-8">
<title>Domino Night Scorecard</title>
<link rel="stylesheet" href="https://fonts.googleapis.com/css2?family=Playfair+Display:wght@400;700;900&display=swap">
<style>
  :root {
    --navy: #223a52;
    --coral: #ff5e42;
    --mint: #5cd6a0;
    --cream: #fdf9ee;
    --rule: #7a7a7a;
    --die: #e6e6e6;
  }
  * { box-sizing: border-box; margin: 0; padding: 0; }
  html, body { width: 746px; height: 1200px; overflow: hidden; background: var(--navy); }
  body { font-family: "Playfair Display", Georgia, serif; position: relative; }

  .masthead { position: absolute; left: 0; top: 0; width: 746px; height: 217px; background: var(--navy); }
  .roller { position: absolute; top: 66px; height: 88px; width: 40px; background: var(--mint); border-radius: 14px; }
  .roller::before { content: ""; position: absolute; top: 12px; height: 64px; width: 18px; background: var(--coral); border-radius: 8px; }
  .roller.left { left: 16px; }
  .roller.left::before { left: -13px; }
  .roller.right { right: 16px; }
  .roller.right::before { right: -13px; }
  .banner {
    position: absolute; left: 58px; top: 43px; width: 632px; height: 138px;
    background: var(--cream); border: 5px solid var(--coral); border-radius: 22px;
    display: flex; flex-direction: column; align-items: center; justify-content: center;
    color: var(--navy); text-shadow: 2px 3px 3px rgba(0,0,0,.35); line-height: .92;
  }
  .banner .line-one { font-size: 67px; font-weight: 900; letter-spacing: 1px; }
  .banner .line-two { font-size: 48px; font-weight: 900; }
  .date-tab {
    position: absolute; left: 285px; top: 181px; width: 177px; height: 21px;
    background: var(--cream); border-radius: 0 0 8px 8px;
    font-size: 14px; color: var(--navy); text-align: center; line-height: 21px;
  }

  .score-table {
    position: absolute; left: 0; top: 217px; width: 746px; height: 983px;
    display: grid;
    grid-template-columns: 130px 48px repeat(6, 1fr);
    grid-template-rows: 61px repeat(6, 61px) 67px repeat(7, 61px) 62px;
  }
  .label {
    grid-column: 1 / 3; background: var(--cream); color: var(--navy);
    display: flex; align-items: center; justify-content: center; text-align: center;
    font-size: 24px; line-height: 1; box-shadow: inset -4px 0 6px rgba(0,0,0,.12);
  }
  .label.game { font-size: 23px; white-space: nowrap; }
  .player {
    background: var(--coral); color: var(--navy); font-size: 18px; text-transform: uppercase;
    display: flex; align-items: center; justify-content: center; border-left: 1px solid #b8432e;
  }
  .dice { background: var(--navy); display: flex; align-items: center; justify-content: center; gap: 12px; border-bottom: 1px solid #1a2d40; }
  .die { width: 36px; height: 38px; border-radius: 7px; background: var(--die); box-shadow: 2px 3px 4px rgba(0,0,0,.4); }
  .value {
    background: var(--mint); color: #fff; font-size: 28px; font-weight: 700;
    display: flex; align-items: center; justify-content: center;
    text-shadow: 1px 2px 2px rgba(0,0,0,.35); border-bottom: 1px solid #4dbd8b;
  }
  .cell { background: var(--cream); border-left: 1px solid var(--rule); border-bottom: 1px solid var(--rule); }
  .total { background: var(--coral); border-left: 1px solid #b8432e; border-top: 1px solid var(--rule); }
</style>
</head>
<body>
  <header class="masthead">
    <div class="roller left"></div>
    <div class="roller right"></div>
    <div class="banner">
      <div class="line-one">MEXICAN TRAIN</div>
      <div class="line-two">DOMINOS SCORECARD</div>
    </div>
    <div class="date-tab">DATE:6/14/2020</div>
  </header>

  <main class="score-table">
    <div class="label">PLAYER’S<br>NAME</div>
    <div class="player">Tessa</div><div class="player">Harold</div><div class="player">Ruth</div>
    <div class="player">Colin</div><div class="player">Dana</div><div class="player">Iris</div>

    <div class="dice"><div class="die" role="img" aria-label="die showing 12"></div><div class="die" role="img" aria-label="die showing 12"></div></div><div class="value">12</div>
    <div class="cell"></div><div class="cell"></div><div class="cell"></div><div class="cell"></div><div class="cell"></div><div class="cell"></div>
    <div class="dice"><div class="die" role="img" aria-label="die showing 11"></div><div class="die" role="img" aria-label="die showing 11"></div></div><div class="value">11</div>
    <div class="cell"></div><div class="cell"></div><div class="cell"></div><div class="cell"></div><div class="cell"></div><div class="cell"></div>
    <div class="dice"><div class="die" role="img" aria-label="die showing 10"></div><div class="die" role="img" aria-label="die showing 10"></div></div><div class="value">10</div>
    <div class="cell"></div><div class="cell"></div><div class="cell"></div><div class="cell"></div><div class="cell"></div><div class="cell"></div>
    <div class="dice"><div class="die" role="img" aria-label="die showing 9"></div><div class="die" role="img" aria-label="die showing 9"></div></div><div class="value">9</div>
    <div class="cell"></div><div class="cell"></div><div class="cell"></div><div class="cell"></div><div class="cell"></div><div class="cell"></div>
    <div class="dice"><div class="die" role="img" aria-label="die showing 8"></div><div class="die" role="img" aria-label="die showing 8"></div></div><div class="value">8</div>
    <div class="cell"></div><div class="cell"></div><div class="cell"></div><div class="cell"></div><div class="cell"></div><div class="cell"></div>
    <div class="dice"><div class="die" role="img" aria-label="die showing 7"></div><div class="die" role="img" aria-label="die showing 7"></div></div><div class="value">7</div>
    <div class="cell"></div><div class="cell"></div><div class="cell"></div><div class="cell"></div><div class="cell"></div><div class="cell"></div>

    <div class="label">SUB TOTAL</div>
    <div class="total"></div><div class="total"></div><div class="total"></div><div class="total"></div><div class="total"></div><div class="total"></div>

    <div class="dice"><div class="die" role="img" aria-label="die showing 6"></div><div class="die" role="img" aria-label="die showing 6"></div></div><div class="value">6</div>
    <div class="cell"></div><div class="cell"></div><div class="cell"></div><div class="cell"></div><div class="cell"></div><div class="cell"></div>
    <div class="dice"><div class="die" role="img" aria-label="die showing 5"></div><div class="die" role="img" aria-label="die showing 5"></div></div><div class="value">5</div>
    <div class="cell"></div><div class="cell"></div><div class="cell"></div><div class="cell"></div><div class="cell"></div><div class="cell"></div>
    <div class="dice"><div class="die" role="img" aria-label="die showing 4"></div><div class="die" role="img" aria-label="die showing 4"></div></div><div class="value">4</div>
    <div class="cell"></div><div class="cell"></div><div class="cell"></div><div class="cell"></div><div class="cell"></div><div class="cell"></div>
    <div class="dice"><div class="die" role="img" aria-label="die showing 3"></div><div class="die" role="img" aria-label="die showing 3"></div></div><div class="value">3</div>
    <div class="cell"></div><div class="cell"></div><div class="cell"></div><div class="cell"></div><div class="cell"></div><div class="cell"></div>
    <div class="dice"><div class="die" role="img" aria-label="die showing 2"></div><div class="die" role="img" aria-label="die showing 2"></div></div><div class="value">2</div>
    <div class="cell"></div><div class="cell"></div><div class="cell"></div><div class="cell"></div><div class="cell"></div><div class="cell"></div>
    <div class="dice"><div class="die" role="img" aria-label="die showing 1"></div><div class="die" role="img" aria-label="die showing 1"></div></div><div class="value">1</div>
    <div class="cell"></div><div class="cell"></div><div class="cell"></div><div class="cell"></div><div class="cell"></div><div class="cell"></div>
    <div class="dice"><div class="die" role="img" aria-label="blank die"></div><div class="die" role="img" aria-label="blank die"></div></div><div class="value">0</div>
    <div class="cell"></div><div class="cell"></div><div class="cell"></div><div class="cell"></div><div class="cell"></div><div class="cell"></div>

    <div class="label game">GAME TOTAL</div>
    <div class="total"></div><div class="total"></div><div class="total"></div><div class="total"></div><div class="total"></div><div class="total"></div>
  </main>
</body>
</html>
```